Atelier Marrow Architecture business card

We need to update our business card. We do high end custom residential, hospitality, and wellness architecture. We focus on creating unique spaces and design around the five senses, believing that architecture's true impact is not on our surroundings, but within us. We would like to see designs are instill a sense of calm awe. They should be crisp, fresh, clean, authentic, & contemporary without being sterile, overworked, or harsh. White space is important. Alternative materials are an option if natural. We have created our own logo and would like designs to incorporate it. However, we are willing to see alternatives if the logo becomes a stumbling block and you have an alternate you suggest. Card must have the following information:
Atelier Marrow Architecture, Inc.
728 Holloway Ct. NE Atlanta, GA 30318
Marcus T. Whitcombe, AIA, NCARB, LEED AP BD+C
ateliermarrow.example

Target Market(s)

Higher net worth individuals with an appreciation for design, nature, sustainability,

Industry/Entity Type

Architect

Contact Information for Business Card

See above. The title of Owner or Architect is helpful but not necessary. Minimalism should trump additional information.

Font styles to use
Serif
Sans Serif

Requirements
Must have
• It should look professional. It must use logo
Should not have
• caligraphy, animals, anything that is cute,

```html
<!DOCTYPE html>
<html lang="en">
<head>
<meta charset="utf-8">
<title>Atelier Marrow Architecture – Business Card</title>
<link href="https://fonts.googleapis.com/css2?family=Source+Sans+3:wght@400;600&display=swap" rel="stylesheet">
<style>
  :root {
    --backdrop: #5a4a3d;
    --paper: #f6f6f4;
    --forest: #0f5438;
    --forest-text: #0b4a30;
    --ink: #3a3a3a;
    --address: #4a4a4a;
    --rule: #b9b9b9;
    --white: #ffffff;
  }
  * { margin: 0; padding: 0; box-sizing: border-box; }
  html, body {
    width: 1200px;
    height: 987px;
    overflow: hidden;
    background: var(--backdrop);
  }
  .canvas {
    position: relative;
    width: 1200px;
    height: 987px;
  }
  .card {
    position: absolute;
    left: 293px;
    width: 615px;
    height: 351px;
    box-shadow: 0 3px 8px rgba(0, 0, 0, 0.35);
  }
  .card--front { top: 130px; background: var(--paper); }
  .card--back  { top: 505px; background: var(--forest); }

  .brand-name {
    position: absolute;
    left: 0;
    right: 0;
    text-align: center;
    font-family: "Source Sans 3", sans-serif;
    font-weight: 400;
    font-size: 26px;
    line-height: 1;
    letter-spacing: 0.02em;
  }
  .card--front .brand-name { top: 78px; color: var(--ink); }
  .card--back  .brand-name { top: 160px; color: var(--white); }

  .contact {
    position: absolute;
    left: 49px;
    right: 49px;
    top: 258px;
    text-align: center;
    font-family: "Source Sans 3", sans-serif;
  }
  .contact__name {
    font-size: 22px;
    font-weight: 600;
    color: var(--forest-text);
    line-height: 1.2;
  }
  .contact__credentials {
    font-size: 15px;
    font-weight: 600;
  }
  .contact__rule {
    height: 1px;
    background: var(--rule);
    margin: 6px 0 10px;
  }
  .contact__details {
    font-size: 16px;
    font-weight: 400;
    color: var(--address);
    line-height: 1.2;
  }
  .contact__divider { margin: 0 6px; }
</style>
</head>
<body>
<main class="canvas">
  <section class="card card--front" aria-label="Business card front">
    <p class="brand-name">Atelier Marrow Architecture</p>
    <div class="contact">
      <p class="contact__name">Marcus T. Whitcombe,<span class="contact__credentials"> AIA, NCARB, LEED AP BD+C</span></p>
      <div class="contact__rule"></div>
      <p class="contact__details">728 Holloway Ct. NE Atlanta, GA 30318<span class="contact__divider">|</span>www.ateliermarrow.example</p>
    </div>
  </section>

  <section class="card card--back" aria-label="Business card back">
    <p class="brand-name">Atelier Marrow Architecture</p>
  </section>
</main>
</body>
</html>
```